Wavelume artwork for new single release

I need Wavelume artwork creating to release a new single on there.

The specs are:

Ideal size: 3000 x 3000 pixels
Minimum size: 1400 x 1400 pixels
Aspect ratio: 1:1 (must be a perfect square)
File format: JPG or PNG
Color space: sRGB
File size: Max 4MB

The song is called "Still, Can We Wander?"
The artist is "Milo Fenwright"

We have no images of Milo, so it really is open to imagination.

Target Market(s)

Wavelume listeners

Industry/Entity Type

Music

```html
<!DOCTYPE html>
<html lang="en">
<head>
<meta charset="utf-8">
<title>Still, Can We Wander? — Single Artwork</title>
<link rel="stylesheet" href="https://fonts.googleapis.com/css2?family=Cinzel:wght@500&family=Open+Sans:wght@400;600&family=Permanent+Marker&display=swap">
<style>
:root{
  --stage:#3f3e43;
  --screen:#141415;
  --bar:#1d1d1f;
  --bar-light:#232326;
  --rule:#070707;
  --green:#2ec45a;
  --green-dark:#1f8f40;
  --white:#ffffff;
  --red:#e04444;
  --text-soft:#d9d9d9;
  --text-mute:#8a8a8d;
  --icon:#c9c9cc;
  --ice-light:#a9aebb;
  --ice-mid:#858b99;
  --ice-dark:#555a66;
}
*{box-sizing:border-box;margin:0;padding:0}
html,body{width:749px;height:1200px;overflow:hidden;background:var(--stage)}
body{position:relative;font-family:"Open Sans",Arial,sans-serif;color:var(--white)}

/* cover artwork */
.cover{position:absolute;overflow:hidden}
.cover-small{font-size:3.16px}
.cover-medium{font-size:5.37px}
.cover-large{font-size:10px}
.cover-art{position:absolute;inset:0;
  background:radial-gradient(ellipse at 50% 45%,var(--ice-light) 0%,var(--ice-mid) 55%,var(--ice-dark) 100%)}
.cover-artist{position:absolute;left:0;right:0;top:4.4%;text-align:center;font-family:"Cinzel",Georgia,serif;font-weight:500;font-size:1.9em;letter-spacing:.42em;color:var(--white);white-space:nowrap}
.cover-title{position:absolute;transform:translateX(-50%);font-family:"Permanent Marker",cursive;line-height:1;white-space:nowrap}
.title-top{left:42%;top:25%;font-size:5.6em;color:var(--white)}
.title-main{left:52%;top:49%;font-size:9em;color:var(--red)}
.title-bottom{left:49%;top:78%;font-size:4.8em;color:var(--white)}

/* phone screens */
.screen{position:absolute;top:74px;width:263px;height:516px;background:var(--screen);overflow:hidden;box-shadow:8px 8px 10px rgba(0,0,0,.35)}
.screen-left{left:75px}
.screen-right{left:378px}
.top-bar{position:absolute;left:0;top:0;width:100%;height:33px;background:var(--bar);border-bottom:5px solid var(--rule)}
.top-bar svg{position:absolute;top:7px}
.glow-band{position:absolute;left:0;width:100%;background:linear-gradient(to bottom,rgba(46,196,90,0),var(--green-dark))}

.album-dots{position:absolute;left:128px;top:192px;display:flex;gap:2px}
.album-dots span{width:3px;height:3px;border-radius:50%;background:#555}
.album-dots span:first-child{background:var(--green)}
.album-button{position:absolute;left:72px;top:205px;width:118px;height:37px;border-radius:19px;background:var(--green);font-size:12px;line-height:37px;text-align:center;letter-spacing:.2px}

.track{position:absolute;left:18px;width:230px;height:30px}
.track-title{font-size:12px;font-weight:600;color:var(--text-soft);line-height:13px}
.track-singer{font-size:12px;color:var(--text-mute);line-height:13px}
.track svg{position:absolute;right:0;top:4px}

.progress{position:absolute;height:2px;background:#3a3a3d}
.progress-fill{height:100%;background:var(--green)}

.mini-player{position:absolute;left:0;width:100%;background:var(--bar-light);font-size:12px;text-align:center}
.mini-player b{font-weight:600;color:var(--text-soft)}
.mini-player span{color:var(--text-mute)}
.mini-player svg{position:absolute}

.nav{position:absolute;left:0;bottom:0;width:100%;height:47px;background:var(--bar-light);border-top:1px solid #111}
.nav-item{position:absolute;top:8px;width:60px;margin-left:-30px;text-align:center;font-size:7.5px;color:var(--text-mute)}
.nav-item.active{color:var(--white);font-weight:600}
.nav-item svg{display:block;margin:0 auto 2px}

.now-title{position:absolute;left:0;right:0;top:312px;text-align:center;font-size:18px;font-weight:600;color:var(--white);letter-spacing:.3px}
.now-singer{position:absolute;left:0;right:0;top:334px;text-align:center;font-size:12px;color:var(--text-mute)}
.time{position:absolute;top:362px;font-size:9px;color:var(--text-mute)}
</style>
</head>
<body>

<!-- Album screen -->
<section class="screen screen-left">
  <header class="top-bar">
    <svg style="left:6px" width="12" height="16" viewBox="0 0 12 16"><path d="M9 2 3 8l6 6" fill="none" stroke="var(--icon)" stroke-width="1.6"/></svg>
    <svg style="left:233px" width="24" height="16" viewBox="0 0 24 16"><path d="M8 14C2 9 1 6 2 4s5-3 6 1c1-4 5-3 6-1s0 5-6 10z" fill="none" stroke="var(--icon)" stroke-width="1.3"/><circle cx="21" cy="3" r="1.3" fill="var(--icon)"/><circle cx="21" cy="8" r="1.3" fill="var(--icon)"/><circle cx="21" cy="13" r="1.3" fill="var(--icon)"/></svg>
  </header>

  <div class="cover cover-small" style="left:63px;top:52px;width:136px;height:136px">
    <div class="cover-art" role="img" aria-label="Frosted ice texture with a small standing figure in black"></div>
    <div class="cover-artist">MILO FENWRIGHT</div>
    <div class="cover-title title-top">Still,</div>
    <div class="cover-title title-main">CAN WE</div>
    <div class="cover-title title-bottom">Wander?</div>
  </div>
  <div class="album-dots"><span></span><span></span><span></span></div>
  <div class="album-button">ALBUM NAME</div>
  <svg style="position:absolute;left:205px;top:209px" width="26" height="26" viewBox="0 0 26 26"><circle cx="13" cy="13" r="11.5" fill="none" stroke="var(--icon)" stroke-width="1.4"/><path d="M13 7v11M8.5 13.5 13 18l4.5-4.5" fill="none" stroke="var(--icon)" stroke-width="1.4"/></svg>
  <div class="glow-band" style="top:243px;height:14px"></div>
  <div style="position:absolute;left:0;top:257px;width:100%;height:6px;background:var(--rule)"></div>

  <div class="track" style="top:280px"><div class="track-title">Song Title</div><div class="track-singer">Singer</div>
    <svg width="54" height="18" viewBox="0 0 54 18"><circle cx="8" cy="9" r="7" fill="none" stroke="var(--icon)" stroke-width="1.3"/><path d="M3 4l10 10" stroke="var(--icon)" stroke-width="1.3"/><path d="M30 16c-6-5-7-8-6-10s5-3 6 1c1-4 5-3 6-1s0 5-6 10z" fill="none" stroke="var(--icon)" stroke-width="1.3"/><circle cx="50" cy="4" r="1.2" fill="var(--icon)"/><circle cx="50" cy="9" r="1.2" fill="var(--icon)"/><circle cx="50" cy="14" r="1.2" fill="var(--icon)"/></svg></div>
  <div class="track" style="top:321px"><div class="track-title">Song Title</div><div class="track-singer">Singer</div>
    <svg width="54" height="18" viewBox="0 0 54 18"><circle cx="8" cy="9" r="7" fill="none" stroke="var(--icon)" stroke-width="1.3"/><path d="M3 4l10 10" stroke="var(--icon)" stroke-width="1.3"/><path d="M30 16c-6-5-7-8-6-10s5-3 6 1c1-4 5-3 6-1s0 5-6 10z" fill="none" stroke="var(--icon)" stroke-width="1.3"/><circle cx="50" cy="4" r="1.2" fill="var(--icon)"/><circle cx="50" cy="9" r="1.2" fill="var(--icon)"/><circle cx="50" cy="14" r="1.2" fill="var(--icon)"/></svg></div>
  <div class="track" style="top:362px"><div class="track-title">Song Title</div><div class="track-singer">Singer</div>
    <svg width="54" height="18" viewBox="0 0 54 18"><circle cx="8" cy="9" r="7" fill="none" stroke="var(--icon)" stroke-width="1.3"/><path d="M3 4l10 10" stroke="var(--icon)" stroke-width="1.3"/><path d="M30 16c-6-5-7-8-6-10s5-3 6 1c1-4 5-3 6-1s0 5-6 10z" fill="none" stroke="var(--icon)" stroke-width="1.3"/><circle cx="50" cy="4" r="1.2" fill="var(--icon)"/><circle cx="50" cy="9" r="1.2" fill="var(--icon)"/><circle cx="50" cy="14" r="1.2" fill="var(--icon)"/></svg></div>
  <div class="track" style="top:403px"><div class="track-title">Song Title</div><div class="track-singer">Singer</div>
    <svg width="54" height="18" viewBox="0 0 54 18"><circle cx="8" cy="9" r="7" fill="none" stroke="var(--icon)" stroke-width="1.3"/><path d="M3 4l10 10" stroke="var(--icon)" stroke-width="1.3"/><path d="M30 16c-6-5-7-8-6-10s5-3 6 1c1-4 5-3 6-1s0 5-6 10z" fill="none" stroke="var(--icon)" stroke-width="1.3"/><circle cx="50" cy="4" r="1.2" fill="var(--icon)"/><circle cx="50" cy="9" r="1.2" fill="var(--icon)"/><circle cx="50" cy="14" r="1.2" fill="var(--icon)"/></svg></div>

  <div class="progress" style="left:0;top:434px;width:263px"><div class="progress-fill" style="width:225px"></div></div>
  <div class="mini-player" style="top:436px;height:33px;line-height:33px">
    <svg style="left:6px;top:5px" width="23" height="23" viewBox="0 0 23 23"><circle cx="11.5" cy="11.5" r="11.5" fill="var(--green)"/><path d="M7 9h9l-4.5 6z" fill="var(--white)"/></svg>
    <b>Singer</b> <span>– Song Title</span>
    <svg style="left:241px;top:11px" width="16" height="10" viewBox="0 0 16 10"><path d="M1 9l7-7 7 7" fill="none" stroke="var(--white)" stroke-width="1.6"/></svg>
  </div>

  <nav class="nav">
    <div class="nav-item" style="left:28px"><svg width="18" height="20" viewBox="0 0 18 20"><path d="M2 9 9 2l7 7v9h-5v-5H7v5H2z" fill="none" stroke="var(--text-mute)" stroke-width="1.3"/></svg>Home</div>
    <div class="nav-item" style="left:98px"><svg width="18" height="20" viewBox="0 0 18 20"><rect x="1.5" y="4" width="15" height="14" fill="none" stroke="var(--text-mute)" stroke-width="1.3"/><path d="M3 1.5h12" stroke="var(--text-mute)" stroke-width="1.3"/><circle cx="9" cy="11" r="3.5" fill="none" stroke="var(--text-mute)" stroke-width="1.3"/></svg>Browser</div>
    <div class="nav-item" style="left:167px"><svg width="18" height="20" viewBox="0 0 18 20"><circle cx="9" cy="9" r="7.5" fill="none" stroke="var(--text-mute)" stroke-width="1.3"/><path d="M14 15l3 3" stroke="var(--text-mute)" stroke-width="1.3"/></svg>Search</div>
    <div class="nav-item active" style="left:237px"><svg width="18" height="20" viewBox="0 0 18 20"><path d="M2 2v16M6 2v16M9 2l6 16" stroke="var(--white)" stroke-width="2"/></svg>Library</div>
  </nav>
</section>

<!-- Now playing screen -->
<section class="screen screen-right">
  <header class="top-bar">
    <svg style="left:6px" width="12" height="16" viewBox="0 0 12 16"><path d="M9 2 3 8l6 6" fill="none" stroke="var(--icon)" stroke-width="1.6"/></svg>
    <svg style="left:233px" width="24" height="16" viewBox="0 0 24 16"><path d="M8 14C2 9 1 6 2 4s5-3 6 1c1-4 5-3 6-1s0 5-6 10z" fill="none" stroke="var(--icon)" stroke-width="1.3"/><circle cx="21" cy="3" r="1.3" fill="var(--icon)"/><circle cx="21" cy="8" r="1.3" fill="var(--icon)"/><circle cx="21" cy="13" r="1.3" fill="var(--icon)"/></svg>
  </header>

  <div class="cover cover-medium" style="left:16px;top:46px;width:231px;height:231px">
    <div class="cover-art" role="img" aria-label="Frosted ice texture with a small standing figure in black"></div>
    <div class="cover-artist">MILO FENWRIGHT</div>
    <div class="cover-title title-top">Still,</div>
    <div class="cover-title title-main">CAN WE</div>
    <div class="cover-title title-bottom">Wander?</div>
  </div>

  <svg style="position:absolute;left:23px;top:325px" width="10" height="14" viewBox="0 0 10 14"><path d="M2 4l6 6-3 3V1l3 3-6 6" fill="none" stroke="#444" stroke-width="1"/></svg>
  <div class="now-title">SONG TITLE</div>
  <div class="now-singer">Singer</div>
  <svg style="position:absolute;left:226px;top:328px" width="14" height="10" viewBox="0 0 14 10"><path d="M0 2h3l6 6h4M0 8h3l6-6h4" fill="none" stroke="#444" stroke-width="1"/></svg>

  <div class="progress" style="left:16px;top:360px;width:231px"><div class="progress-fill" style="width:193px"></div></div>
  <div style="position:absolute;left:206px;top:358px;width:6px;height:6px;border-radius:50%;background:var(--green)"></div>
  <div class="time" style="left:16px">3:45</div>
  <div class="time" style="right:16px">4:49</div>

  <svg style="position:absolute;left:27px;top:404px" width="16" height="14" viewBox="0 0 16 14"><path d="M8 14C1 9 0 6 1 3s5-4 7 0c2-4 6-3 7 0s0 6-7 11z" fill="var(--green)"/></svg>
  <svg style="position:absolute;left:76px;top:404px" width="14" height="16" viewBox="0 0 14 16"><rect x="0" y="1" width="2.5" height="14" fill="var(--icon)"/><path d="M14 1v14L3 8z" fill="var(--icon)"/></svg>
  <svg style="position:absolute;left:114px;top:394px" width="36" height="36" viewBox="0 0 36 36"><circle cx="18" cy="18" r="17" fill="none" stroke="var(--icon)" stroke-width="1.4"/><path d="M15 10v16M21 10v16" stroke="var(--icon)" stroke-width="1.6"/></svg>
  <svg style="position:absolute;left:174px;top:404px" width="14" height="16" viewBox="0 0 14 16"><path d="M0 1v14l11-7z" fill="var(--icon)"/><rect x="11.5" y="1" width="2.5" height="14" fill="var(--icon)"/></svg>
  <svg style="position:absolute;left:221px;top:403px" width="15" height="15" viewBox="0 0 24 24"><path d="M12 1l3.3 7 7.7.8-5.8 5.2 1.7 7.6L12 17.7 5.1 21.6l1.7-7.6L1 8.8 8.7 8z" fill="var(--green)"/></svg>

  <div class="glow-band" style="top:465px;height:17px"></div>
  <svg style="position:absolute;left:13px;top:464px" width="10" height="8" viewBox="0 0 10 8"><path d="M0 1h10M0 4h10M0 7h10" stroke="var(--icon)" stroke-width="1"/></svg>
  <svg style="position:absolute;left:242px;top:461px" width="14" height="14" viewBox="0 0 14 14"><circle cx="7" cy="7" r="6" fill="none" stroke="var(--icon)" stroke-width="1"/><path d="M7 3.5v6M4.5 7.5 7 10l2.5-2.5" fill="none" stroke="var(--icon)" stroke-width="1"/></svg>

  <div class="mini-player" style="top:482px;height:34px;line-height:34px">
    <svg style="left:6px;top:5px" width="23" height="23" viewBox="0 0 23 23"><circle cx="11.5" cy="11.5" r="11.5" fill="var(--green)"/><path d="M9 7v9M14 7v9" stroke="var(--white)" stroke-width="1.8"/></svg>
    <b>Singer</b> <span>– Song Title</span>
    <svg style="left:241px;top:12px" width="16" height="10" viewBox="0 0 16 10"><path d="M1 9l7-7 7 7" fill="none" stroke="var(--white)" stroke-width="1.6"/></svg>
  </div>
</section>

<!-- Full single artwork -->
<section class="cover cover-large" style="left:159px;top:700px;width:430px;height:430px">
  <div class="cover-art" role="img" aria-label="Frosted ice texture with a small standing figure in black beside the title"></div>
  <div class="cover-artist">MILO FENWRIGHT</div>
  <div class="cover-title title-top">Still,</div>
  <div class="cover-title title-main">CAN WE</div>
  <div class="cover-title title-bottom">Wander?</div>
</section>

</body>
</html>
```